KRL Banner Logo with Rocky Mountain of CO as the background

I need a banner/logo for my KRL year. So have a banner design that is like an intentional path or inspiring.

• KRL Silver Ridge CO mountain as background and they may add similar images that I sent you
• Wording: Intentional Path
Learning year 2025-2026
• Add the KRL logo (the white and blue image – you will see these online)

UPDATE: Attached are example images on how we envision the banner. Please do not use the attached example sample images. Kindly look for similar looking images that are FREE TO USE Commercially.

CEO, top executives

0054AA
0677BA
7BADD7
CADEEF
E8F1F8

• • KRL Silver Ridge CO mountain as background and they may add similar images that I sent you • Wording: Intentional Path Learning year 2025-2026 • Add the KRL logo (the white and blue image – you will see these online)
• It has nice to have the inspirational images attached but you can have your own design. This is only for sample.

```html
<!DOCTYPE html>
<html lang="en">
<head>
<meta charset="utf-8">
<title>KRL Silver Ridge – Intentional Path Learning Year 2025-2026</title>
<link rel="stylesheet" href="https://fonts.googleapis.com/css2?family=Arimo:wght@700&display=swap">
<style>
  :root {
    --stage: #000000;
    --sky-top: #d8c9a6;
    --sky-glow: #e6c98a;
    --ridge: #a9a8a6;
    --slope: #6f7580;
    --base: #3a3f48;
    --title-fill: #1d232d;
    --title-edge: #e6edf3;
    --subtitle: #ffffff;
    --mark: #1b2a5c;
  }
  html, body {
    margin: 0;
    padding: 0;
    width: 1200px;
    height: 420px;
    overflow: hidden;
    background: var(--stage);
  }
  .canvas {
    position: relative;
    width: 1200px;
    height: 420px;
    background: var(--stage);
  }
  .banner {
    position: absolute;
    left: 210px;
    top: 120px;
    width: 780px;
    height: 180px;
    overflow: hidden;
  }
  .banner-photo {
    position: absolute;
    inset: 0;
    background:
      radial-gradient(ellipse 45% 60% at 95% 55%, var(--sky-glow) 0%, rgba(230,201,138,0) 70%),
      linear-gradient(180deg, var(--sky-top) 0%, var(--ridge) 38%, var(--slope) 62%, var(--base) 100%);
  }
  .banner-brand {
    position: absolute;
    right: 30px;
    top: 22px;
    display: flex;
    align-items: center;
    gap: 10px;
    font-family: "Arimo", Arial, sans-serif;
    font-weight: 700;
    font-size: 30px;
    line-height: 1;
    color: var(--mark);
  }
  .banner-brand__square {
    width: 34px;
    height: 34px;
    background: var(--mark);
  }
  .banner-type {
    position: absolute;
    inset: 0;
  }
  .banner-type__title {
    font-family: "Arimo", Arial, sans-serif;
    font-weight: 700;
    font-size: 72px;
    fill: var(--title-fill);
    stroke: var(--title-edge);
    stroke-width: 2;
    paint-order: stroke;
    filter: drop-shadow(2px 3px 2px rgba(0,0,0,0.55));
  }
  .banner-type__subtitle {
    font-family: "Arimo", Arial, sans-serif;
    font-weight: 700;
    font-size: 32px;
    fill: var(--subtitle);
    filter: drop-shadow(2px 2px 2px rgba(0,0,0,0.6));
  }
</style>
</head>
<body>
  <main class="canvas">
    <section class="banner">
      <div class="banner-photo" role="img" aria-label="Photograph of snow-capped Rocky Mountain peaks under a golden sky, with a stacked stone cairn lit by sunlight on the left"></div>
      <div class="banner-brand">
        <span class="banner-brand__square"></span>
        <span class="banner-brand__name">KRL</span>
      </div>
      <svg class="banner-type" width="780" height="180" viewBox="0 0 780 180">
        <text class="banner-type__title" x="156" y="115" textLength="600" lengthAdjust="spacingAndGlyphs">INTENTIONAL PATH</text>
        <text class="banner-type__subtitle" x="336" y="162" textLength="420" lengthAdjust="spacingAndGlyphs">LEARNING YEAR 2025-2026</text>
      </svg>
    </section>
  </main>
</body>
</html>
```